Varnok Immigration _Cloud-based, boutique law firm serving clients worldwide in US Immigration Law

I need a website for my new US immigration law firm that will be based in Montreal, QC Canada but serve clients worldwide to achieve their US immigration goals. This will be a boutique firm offering attentive and compassionate service to our corporate and individual clients. I'd like the site to be fresh, modern, sophisticated and easy to read.

I will need a home page, about/bio page, services page, and contact me page with a form so potential clients could email inquiries and also schedule consultations. I would also like a 'Book a Consultation' button on the home page (easily visible).

The longest website page is going to be the 'Services' tab, which I'd like to break down to services for Employers and services Individuals, with further sub-sets of services to each type of client. I envision images with short text that display longer text when hoovering over.

To start, I would have 3 subsets of services for Employers and 5 subsets of services for Individuals. I will need the ability to expand/edit these pages in Wix interface as we grow.

The site will need to be in English and in French.

I like the color blue and the final design should communicate the firm's core values: integrity and compassion. In other words, we do right, no matter what and are understanding to individual circumstances. I'd like the site to convey sophistication and accessibility. I don't like staged stock photos of people. Sites with a lot of stock photos of people feels unauthentic to me.

Logo draft is attached in jpeg. Navy and gold colors.
Example of 4 law firm sites I like below:
- https://www.halvenlawqtz.example/
-https://www.trivolaw.example/
-https://kestrimappeals.example/
-https://www.unbralaw.example/

Target Market(s)

Small-medium sized businesses (10-999 employees) in US with foreign workforce; Foreign entrepreneurs wishing to implant in the US

Industry/Entity Type

Law

Coding

Coded - Design and coding required

Font styles to use
Sans Serif

Colors

Designer to choose colors to be used in the design.

Requirements
Must have
• Great Home Page (Grabs attention with eye-catching images/text; Immediately establishes credibility; Provides an overview of services; Encourages visitor to take the next action.)
Nice to have
• Images of Montreal (where firm is based); Images of bridges (symbolizes progress, movement, connections)
Should not have
• Non-authentic photos: staged people at desks or pictures of court buildings.

```html
<!DOCTYPE html>
<html lang="en">
<head>
<meta charset="utf-8">
<title>Varnok Immigration</title>
<link href="https://fonts.googleapis.com/css2?family=Montserrat:wght@400;500;600;700&display=swap" rel="stylesheet">
<style>
:root{
  --navy:#333a55;
  --navy-deep:#2c3452;
  --blue:#0b4a8b;
  --gold:#a89572;
  --ink:#222630;
  --muted:#6b6f7a;
  --paper:#ffffff;
  --mist:#f6f6f7;
  --line:#b9bcc4;
}
*{box-sizing:border-box;margin:0;padding:0}
html,body{width:1200px;height:3275px;overflow:hidden}
body{position:relative;font-family:"Montserrat",sans-serif;color:var(--ink);background:var(--paper)}
.abs{position:absolute}
.btn{position:absolute;display:flex;align-items:center;justify-content:center;font-weight:600;letter-spacing:1.6px;font-size:14px;text-transform:uppercase}
.btn-light{background:#fff;color:var(--blue)}
.btn-blue{background:var(--blue);color:#fff}

/* header */
.header-brand{left:0;top:0;width:433px;height:159px;background:var(--navy)}
.header-top{left:433px;top:0;width:767px;height:79px;background:#fff}
.header-nav{left:433px;top:79px;width:767px;height:80px;background:var(--navy)}
.brand{left:94px;top:46px;display:flex;align-items:center;gap:14px}
.brand-mark{width:70px;height:70px;border-radius:50%;background:var(--gold);opacity:.85}
.brand-name{color:var(--gold);font-weight:500;font-size:23px;letter-spacing:3px;line-height:30px;text-transform:uppercase}
.brand-sub{color:var(--gold);font-weight:500;font-size:10px;letter-spacing:2px;text-transform:uppercase;margin-top:4px}
.eval{left:658px;top:30px;font-size:13px;font-weight:500;color:var(--ink)}
.top-cta{left:838px;top:20px;width:204px;height:37px;background:var(--navy);color:#fff;border-radius:6px 6px 0 0;font-size:14px}
.nav{top:106px;color:#fff;font-size:13.5px;font-weight:500;text-transform:uppercase}
.lang{left:994px;top:98px;width:57px;height:30px;border:1px solid #fff;color:#fff;font-size:13px;display:flex;align-items:center;padding-left:9px;gap:12px}

/* hero */
.hero{left:0;top:159px;width:1200px;height:557px;background:linear-gradient(180deg,#5d6d85 0%,#6a7a90 45%,#7a6a5e 80%,#5d5a58 100%)}
.hero-sub{left:0;width:1200px;top:282px;text-align:center;color:#fff;font-size:20px;line-height:29px;font-weight:400}
.hero-title{left:0;width:1200px;top:354px;text-align:center;color:#fff;font-size:56px;font-weight:600}

/* services */
.section-title{left:0;width:1200px;text-align:center;font-size:28px;color:var(--ink)}
.section-title b{font-weight:700}
.bridge{left:0;top:1030px;width:600px;height:606px;background:linear-gradient(90deg,#a6b4c6 0%,#c3ccd8 50%,rgba(255,255,255,0) 100%)}
.card{background:#fff;border-radius:18px;box-shadow:0 14px 40px rgba(70,90,200,.16)}
.card-title{font-size:32px;font-weight:600;color:var(--navy)}
.card-rule{height:3px;width:122px;background:var(--blue)}
.card-text{font-size:13.5px;line-height:18.5px;color:var(--ink);width:250px}

.about-bar{left:642px;top:1226px;width:4px;height:62px;background:var(--blue)}
.about-title{left:658px;top:1224px;font-size:28px;line-height:33px;color:var(--navy)}
.about-title b{font-weight:700}
.about-text{left:636px;top:1330px;width:400px;font-size:15.5px;line-height:23.5px;color:var(--ink)}
.about-link{left:642px;top:1477px;font-size:17px;font-weight:600;color:var(--blue);display:flex;align-items:center;gap:12px}

/* band */
.band{left:0;top:1636px;width:1200px;height:309px;background:var(--navy);border-top-right-radius:58px}
.band-text{left:0;width:1200px;top:1719px;text-align:center;color:#fff;font-size:28px;line-height:33px}

/* why */
.why{left:0;top:1945px;width:1200px;height:560px;background:var(--mist)}
.skyline{left:0;top:2345px;width:1200px;height:617px;background:linear-gradient(90deg,#e8b4b4 0%,#f2dede 20%,#f8f8f9 40%,#f8f8f9 60%,#d9e0e8 80%,#a9b8c8 100%)}
.why-title{left:0;width:1200px;top:1994px;text-align:center;font-size:28px;font-weight:600;color:var(--navy)}
.divider{width:1px;background:#444}
.feat-title{font-size:21px;font-weight:600;color:var(--navy)}
.feat-text{font-size:13.5px;line-height:20px;width:210px;color:var(--ink)}

/* footer */
.footer{left:0;top:2962px;width:1200px;height:313px;background:var(--navy)}
.foot-brand{left:133px;top:3070px;display:flex;align-items:center;gap:8px}
.foot-brand .brand-mark{width:34px;height:34px}
.foot-brand .brand-name{font-size:12px;line-height:14px;letter-spacing:1.5px}
.foot-label{color:#fff;font-size:14px;font-weight:600}
.foot-item{color:#fff;font-size:14px;display:flex;align-items:center;gap:12px}
.quick{left:727px;color:#fff;font-size:13.5px}
.social{top:3050px;width:26px;height:26px;border-radius:50%;background:#fff}

/* form */
.form-layer{z-index:2}
.form-box{left:214px;top:2501px;width:771px;height:506px;background:#fff;box-shadow:0 4px 14px rgba(0,0,0,.12)}
.form-title{left:214px;width:771px;top:2566px;text-align:center;font-size:26px;font-weight:500;color:var(--ink)}
.form-sub{left:214px;width:771px;top:2616px;text-align:center;font-size:16.5px;color:var(--ink)}
.field{border:1.5px solid var(--line);font-size:12.5px;color:var(--muted);padding:8px 10px;background:#fff}
</style>
</head>
<body>

<!-- header -->
<div class="abs header-brand"></div>
<div class="abs header-top"></div>
<div class="abs header-nav"></div>
<div class="abs brand">
  <div class="brand-mark"></div>
  <div>
    <div class="brand-name">Varnok<br>Immigration</div>
    <div class="brand-sub">Mara Varnok, Attorney</div>
  </div>
</div>
<div class="abs eval">Free Case Evaluation</div>
<div class="btn top-cta">Book Consultation</div>
<div class="abs nav" style="left:576px">Home</div>
<div class="abs nav" style="left:647px">About Us</div>
<div class="abs nav" style="left:746px">Our Services
  <svg width="12" height="8" viewBox="0 0 12 8" style="margin-left:5px"><path d="M1 1l5 5 5-5" fill="none" stroke="#fff" stroke-width="1.3"/></svg></div>
<div class="abs nav" style="left:893px">Contact</div>
<div class="abs lang">EN <svg width="12" height="8" viewBox="0 0 12 8"><path d="M1 1l5 5 5-5" fill="none" stroke="#fff" stroke-width="1.3"/></svg></div>

<!-- hero -->
<div class="abs hero" role="img" aria-label="Photo of the Montreal skyline and old port with a Ferris wheel, under a blue overlay"></div>
<div class="abs hero-sub">Providing the Best Legal Strategy For<br>Your Peace of Mind</div>
<div class="abs hero-title">Your Expert Legal Team</div>
<div class="btn btn-light" style="left:497px;top:549px;width:205px;height:43px">Book Consultation</div>

<!-- services -->
<div class="abs section-title" style="top:766px">Immigration <b>Services</b></div>
<div class="abs bridge" role="img" aria-label="Misty photo of a stone suspension bridge over a river, fading to white"></div>

<div class="abs card" style="left:158px;top:849px;width:424px;height:275px"></div>
<div class="abs card-title" style="left:216px;top:874px">Employers</div>
<div class="abs card-rule" style="left:216px;top:917px"></div>
<div class="abs card-text" style="left:216px;top:934px">From small local businesses to the world’s largest companies, we can support all of your immigration needs, all over the world.</div>
<div class="btn btn-blue" style="left:216px;top:1045px;width:206px;height:43px">Learn More</div>

<div class="abs card" style="left:615px;top:849px;width:427px;height:275px"></div>
<div class="abs card-title" style="left:667px;top:874px">Individuals</div>
<div class="abs card-rule" style="left:667px;top:917px"></div>
<div class="abs card-text" style="left:667px;top:932px;width:270px">We offer comprehensive immigration solutions and guidance for individuals, their families and their advisors around the globe.</div>
<div class="btn btn-blue" style="left:667px;top:1045px;width:206px;height:43px">Learn More</div>

<div class="abs about-bar"></div>
<div class="abs about-title"><b>Immigration Attorneys</b><br>in Montreal</div>
<div class="abs about-text">Lorem ipsum dolor sit amet consectetur. At et purus at lacus lorem nibh nulla adipiscing. Lorem cras cursus ut amet nulla. In tincidunt vitae adipiscing gravida sit viverra tortor. Nisl viverra duis nulla aliquam blandit nibh sed neque dignissim.</div>
<div class="abs about-link">More About Us
  <svg width="30" height="12" viewBox="0 0 30 12"><path d="M0 6h28M23 1l5 5-5 5" fill="none" stroke="#0b4a8b" stroke-width="1.5"/></svg></div>

<!-- band -->
<div class="abs band"></div>
<div class="abs band-text">Lorem ipsum dolor sit amet consectetur.<br>Venenatis sit sit in sem. Lacinia nullam</div>
<div class="btn btn-light" style="left:497px;top:1826px;width:205px;height:44px">Book Consultation</div>

<!-- why choose us -->
<div class="abs why"></div>
<div class="abs skyline" role="img" aria-label="Faded photo of city towers in soft red and steel-blue tones"></div>
<div class="abs why-title">Why Choose Us</div>
<div class="abs divider" style="left:452px;top:2091px;height:241px"></div>
<div class="abs divider" style="left:752px;top:2095px;height:242px"></div>

<svg class="abs" style="left:198px;top:2111px" width="66" height="56" viewBox="0 0 66 56" fill="none" stroke="#2c3452" stroke-width="2.5">
  <circle cx="33" cy="10" r="8"/><circle cx="11" cy="17" r="6"/><circle cx="55" cy="17" r="6"/>
  <path d="M20 54V34a13 13 0 0 1 26 0v20z"/><path d="M2 54V36a9 9 0 0 1 15-6M64 54V36a9 9 0 0 0-15-6M2 54h62"/>
</svg>
<div class="abs feat-title" style="left:198px;top:2181px">Client-Focused</div>
<div class="abs feat-text" style="left:202px;top:2218px">Lorem ipsum dolor sit amet consectetur. Dictum tortor cursus vel elit ac velit neque aliquam pulvinar.</div>

<svg class="abs" style="left:495px;top:2118px" width="54" height="46" viewBox="0 0 54 46" fill="none" stroke="#2c3452" stroke-width="2.5">
  <rect x="2" y="10" width="50" height="34" rx="3"/><path d="M19 10V3h16v7M2 22h50M24 22v5h6v-5"/>
</svg>
<div class="abs feat-title" style="left:493px;top:2181px">Highly Experienced</div>
<div class="abs feat-text" style="left:493px;top:2218px">Lorem ipsum dolor sit amet consectetur. Dictum tortor cursus vel elit ac velit neque aliquam pulvinar.</div>

<svg class="abs" style="left:803px;top:2113px" width="56" height="54" viewBox="0 0 56 54" fill="none" stroke="#2c3452" stroke-width="2.2">
  <path d="M28 2v46M10 50h36M6 12h44M10 12L3 30h14zM46 12l-7 18h14zM3 30a7 5 0 0 0 14 0M39 30a7 5 0 0 0 14 0"/><circle cx="28" cy="6" r="3"/>
</svg>
<div class="abs feat-title" style="left:799px;top:2181px">Justice Warriors</div>
<div class="abs feat-text" style="left:800px;top:2218px">Lorem ipsum dolor sit amet consectetur. Dictum tortor cursus vel elit ac velit neque aliquam pulvinar.</div>

<!-- footer -->
<div class="abs footer"></div>
<div class="abs foot-brand">
  <div class="brand-mark"></div>
  <div class="brand-name">Varnok<br>Immigration</div>
</div>
<div class="abs foot-label" style="left:383px;top:3056px">Legal Office</div>
<div class="abs foot-item" style="left:383px;top:3084px;font-size:20px;font-weight:500">
  <svg width="26" height="26" viewBox="0 0 26 26"><circle cx="13" cy="13" r="13" fill="#fff"/><path d="M9 7l3 3-2 2a9 9 0 0 0 4 4l2-2 3 3-2 2c-5 0-10-5-10-10z" fill="#333a55"/></svg>
  0099 555 014</div>
<div class="abs foot-item" style="left:386px;top:3128px">
  <svg width="18" height="20" viewBox="0 0 18 20" fill="none" stroke="#fff" stroke-width="1.5"><path d="M9 19s7-6 7-11A7 7 0 0 0 2 8c0 5 7 11 7 11z"/><circle cx="9" cy="8" r="2.5"/></svg>
  Your place here</div>
<div class="abs foot-item" style="left:386px;top:3164px">
  <svg width="20" height="15" viewBox="0 0 20 15" fill="none" stroke="#fff" stroke-width="1.5"><rect x="1" y="1" width="18" height="13"/><path d="M1 1l9 7 9-7"/></svg>
  info@varnokimmigration.example</div>

<div class="abs quick" style="top:3051px;font-weight:600">QUICK LINKS</div>
<div class="abs quick" style="top:3085px">Home</div>
<div class="abs quick" style="top:3109px">About Us</div>
<div class="abs quick" style="top:3133px">For Employers</div>
<div class="abs quick" style="top:3157px">For individual</div>
<div class="abs quick" style="top:3181px;left:730px">Contact</div>

<div class="abs social" style="left:980px" aria-label="Social link"></div>
<div class="abs social" style="left:1026px" aria-label="Social link"></div>
<div class="abs social" style="left:1072px" aria-label="Social link"></div>

<!-- contact form (sits above the footer) -->
<div class="abs form-box form-layer"></div>
<div class="abs form-title form-layer">Ready to Discuss Your Case?</div>
<div class="abs form-sub form-layer">Fill out the form below and we will be in touch with you shortly.</div>
<div class="abs field form-layer" style="left:320px;top:2678px;width:272px;height:42px">First name</div>
<div class="abs field form-layer" style="left:606px;top:2678px;width:272px;height:42px">Last name</div>
<div class="abs field form-layer" style="left:320px;top:2739px;width:272px;height:42px;padding-left:22px">Phone</div>
<div class="abs field form-layer" style="left:606px;top:2739px;width:272px;height:42px;padding-left:26px">Email</div>
<div class="abs field form-layer" style="left:320px;top:2794px;width:558px;height:110px;padding:20px 12px">How can we help you?</div>
<div class="btn btn-blue form-layer" style="left:524px;top:2930px;width:152px;height:36px">Submit</div>

</body>
</html>
```